Automotive component supplier needs a business card design

We need a business card design for our company called Velmar Global Components Ltd based in the UK. We are a supplier of interior and exterior components to premium car manufacturers such as Corvane Hale, Durrant Fyfe, Maxtorn and Valdessimo. We would like to see a modern business card design that uses the colour blue.

Target Market(s)

Premium automotive car manufacturers.

Industry/Entity Type

Automotive

Contact Information for Business Card

Company Name : Velmar Global Components Limited
Address: 17 Tamsey Yard, Upper Drisk, Warwick, CV31 8RJ, United Kingdom
Web Address : www.velmarparts-example.co.uk

Font styles to use
Other font styles liked:
• Helvetica

Colors
3176b5
0255a3
85acd3
cfdeed
cee9f5
85cae6
34a6d7
0692cd
9bcb3c

Requirements
Must have
• Clear company logo and a mixture of blue colours.
Nice to have
• A high quality modern image.
Should not have
• Multiple colours.

```html
<!DOCTYPE html>
<html lang="en">
<head>
<meta charset="utf-8">
<title>Velmar Global Components – Business Card</title>
<link rel="stylesheet" href="https://fonts.googleapis.com/css2?family=Source+Sans+3:wght@400;600;800&display=swap">
<style>
  :root {
    --brand-blue: #0a8fd0;
    --brand-green: #8dc63f;
    --text-grey: #55595c;
    --card-white: #ffffff;
    --backdrop: #6e4b32;
  }
  html, body {
    margin: 0;
    padding: 0;
    width: 1200px;
    height: 987px;
    overflow: hidden;
    background: var(--backdrop);
    font-family: "Source Sans 3", Helvetica, Arial, sans-serif;
  }
  .canvas {
    position: relative;
    width: 1200px;
    height: 987px;
  }
  .card {
    position: absolute;
    left: 293px;
    width: 615px;
    height: 350px;
    overflow: hidden;
    box-shadow: 0 3px 10px rgba(0, 0, 0, 0.35);
  }
  .card--front { top: 130px; background: var(--card-white); }
  .card--back  { top: 506px; background: var(--brand-blue); }

  .wordmark {
    position: absolute;
    text-align: center;
    font-weight: 800;
    line-height: 1;
  }
  .wordmark__name { display: block; letter-spacing: 1px; }
  .wordmark__tagline { display: block; letter-spacing: 1.5px; }

  .card--front .wordmark {
    left: 40px;
    top: 148px;
    width: 260px;
    color: var(--brand-blue);
  }
  .card--front .wordmark__name { font-size: 50px; }
  .card--front .wordmark__tagline { font-size: 13.5px; margin-top: 4px; }

  .divider {
    position: absolute;
    left: 321px;
    top: 63px;
    width: 1px;
    height: 229px;
    background: #d9dcde;
  }
  .contact {
    position: absolute;
    left: 345px;
    top: 66px;
    color: var(--text-grey);
  }
  .contact__name {
    margin: 0;
    font-size: 24px;
    font-weight: 600;
    color: var(--brand-blue);
    line-height: 1.1;
  }
  .contact__role {
    margin: 1px 0 0;
    font-size: 17.5px;
    color: var(--brand-green);
    line-height: 1.2;
  }
  .contact__address {
    margin: 12px 0 0;
    font-style: normal;
    font-size: 17px;
    line-height: 22px;
  }
  .contact__list {
    list-style: none;
    margin: 8px 0 0;
    padding: 0;
    font-size: 17px;
    line-height: 23.5px;
  }
  .contact__list li { display: flex; align-items: center; }
  .contact__list svg { width: 16px; height: 16px; margin-right: 7px; fill: var(--brand-blue); flex: none; }

  .rule-green {
    position: absolute;
    left: 0; top: 322px;
    width: 100%; height: 2px;
    background: var(--brand-green);
  }
  .band-blue {
    position: absolute;
    left: 0; top: 327px;
    width: 100%; height: 23px;
    background: var(--brand-blue);
  }

  .card--back .wordmark {
    left: 0;
    top: 124px;
    width: 100%;
    color: var(--card-white);
  }
  .card--back .wordmark__name { font-size: 74px; }
  .card--back .wordmark__tagline { font-size: 20px; margin-top: 8px; }
  .back__url {
    position: absolute;
    left: 0; top: 289px;
    width: 100%;
    text-align: center;
    color: var(--card-white);
    font-size: 15.5px;
    letter-spacing: 3px;
  }
</style>
</head>
<body>
<div class="canvas">

  <section class="card card--front">
    <div class="wordmark">
      <span class="wordmark__name">VELMAR</span>
      <span class="wordmark__tagline">GLOBAL COMPONENTS</span>
    </div>
    <div class="divider"></div>
    <div class="contact">
      <h1 class="contact__name">Rowan Ellery</h1>
      <p class="contact__role">CEO/Founder</p>
      <address class="contact__address">
        17 Tamsey Yard, Upper Drisk<br>
        Warwick, CV31 8RJ<br>
        United Kingdom
      </address>
      <ul class="contact__list">
        <li>
          <svg viewBox="0 0 16 16" aria-hidden="true"><path d="M3.2 1.5l2.4 2.6-1.3 1.9c.9 2 2.6 3.7 4.6 4.6l1.9-1.3 2.6 2.4-1.5 2.3C6.6 13.6 2.4 9.4 1 3.6z"/></svg>
          614 220 7391
        </li>
        <li>
          <svg viewBox="0 0 16 16" aria-hidden="true"><path d="M4.5 1h7v14h-7zM5.8 2.6v9.4h4.4V2.6z M7.3 12.8h1.4v1.1H7.3z" fill-rule="evenodd"/></svg>
          752 309 4186
        </li>
        <li>
          <svg viewBox="0 0 16 16" aria-hidden="true"><path d="M1.5 4h13v8.5h-13z M2.5 4.6L8 9l5.5-4.4" /><path d="M2.3 5.2L8 9.6l5.7-4.4" stroke="#fff" stroke-width="1.2" fill="none"/></svg>
          rowan@velmarparts-example.co.uk
        </li>
        <li>
          <svg viewBox="0 0 16 16" aria-hidden="true"><circle cx="8" cy="8" r="6.5"/><path d="M5 4.5c1.5.3 2 1.5 1.3 2.6-.6 1 .4 1.8 1.4 1.6.9 1.4-.2 2.8-.4 4.2M10.5 3.8c-.6 1 .3 1.8 1.3 1.9" stroke="#fff" stroke-width="1" fill="none"/></svg>
          www.velmarparts-example.co.uk
        </li>
      </ul>
    </div>
    <div class="rule-green"></div>
    <div class="band-blue"></div>
  </section>

  <section class="card card--back">
    <div class="wordmark">
      <span class="wordmark__name">VELMAR</span>
      <span class="wordmark__tagline">GLOBAL COMPONENTS</span>
    </div>
    <p class="back__url" style="margin:0">www.velmarparts-example.co.uk</p>
  </section>

</div>
</body>
</html>
```